依頼詳細
お好み焼き屋さんのTOPページのみのデザインをお願いしたいです。
コロナで減少したお客様を呼び戻すために試行錯誤しながら、このたびラーメンも提供することになりましたので、メインはお好み焼き屋さんですが、ラーメンも始めました!という画像付きで告知したいです。

集客を目的としたサイトです。
ターゲットは。お腹が空いた人になります!

レイアウト構成
・ヘッダー(ロゴのみ)
・TOP画像(画像はまだないのでフリーのもので大丈夫です)
・TOPページは画像だけでなくインパクトある感じを希望です(ザックリですみません。)
・お知らせ(3行程度)
・メニュー(テキストのみ)
・店舗情報(2店舗)テキスト
・フッター(下層ページないのでコピーライトぐらいでしょうか)
という構成です。
どこかにツマミドリと味ノートにリンクするボタンが欲しいです。
まだ素材がないため仮のフリー画像で構いません。

初心者の方でも大丈夫です!
今回は予算の都合上、低価格になってしまいましたがデザインのフィーリングが合う方は今後もご依頼する可能性があります!
サイトURL
ページ数
1ページ
希望イメージ
シンプル 複雑
単色 カラフル
暗い 明るい
日常 高級
遊び心 厳粛
未来的 伝統的
女性的 男性的
希望する色
無彩色系
納品ファイル
• 高解像度JPG (.jpg)
• イラストレーター形式 (.ai)
• フォトショップ形式 (.psd)
• PNG形式 (.png)
補足説明
納品はできれば、XDが希望です。
難しい場合はご相談ください。

お客様のイメージに一番近かったため選びました!

この度は、とても素晴らしいデザインのご提案をいただきまして誠にありがとうございました。
どれも捨てがたいデザインなのですが、一番イメージに近いものを選びました。
また、機会がございましたら、ご依頼をさせていただければと思います。
どうぞよろしくお願いいたします。

```html
<!DOCTYPE html>
<html lang="ja">
<head>
<meta charset="utf-8">
<title>お好み焼き店 トップページ</title>
<link href="https://fonts.googleapis.com/css2?family=Noto+Sans+JP:wght@400;700&family=Noto+Serif+JP:wght@500;700&display=swap" rel="stylesheet">
<style>
:root{
  --ink:#222;
  --dark:#1c1b1a;
  --orange:#f29a2e;
  --red:#e2522f;
  --paper:#f3f3f3;
  --line:#d9d9d9;
  --muted:#777;
}
*{box-sizing:border-box;margin:0;padding:0}
html,body{width:1200px;height:2736px;overflow:hidden}
body{position:relative;background:#fff;color:var(--ink);font-family:"Noto Sans JP",sans-serif}
.serif{font-family:"Noto Serif JP",serif}
.btn{display:inline-block;color:#fff;font-size:15px;padding:10px 20px;text-decoration:none;line-height:1}
.btn--orange{background:var(--orange)}
.btn--red{background:var(--red)}

.site-header{position:absolute;top:0;left:0;width:1200px;height:62px;background:rgba(20,20,20,.88);display:flex;align-items:center;justify-content:space-between;padding:0 32px;z-index:3}
.site-header .logo{color:#fff;font-size:22px;font-weight:700;letter-spacing:.08em}
.site-header .btns{display:flex;gap:14px}

.hero{position:absolute;top:0;left:0;width:1200px;height:680px;background:radial-gradient(ellipse at 45% 60%,#b07a48 0%,#6b4127 45%,#2a1a12 100%)}
.hero-line{position:absolute;writing-mode:vertical-rl;white-space:nowrap;color:#fff;text-shadow:0 2px 8px rgba(0,0,0,.5);line-height:1}
.hero-line--1{top:120px;left:800px;font-size:66px;font-weight:700;letter-spacing:.12em}
.hero-line--2{top:230px;left:700px;font-size:66px;font-weight:700;letter-spacing:.12em}
.hero-line--sub{top:390px;left:630px;font-size:32px;font-weight:500;letter-spacing:.18em}
.hero-side{position:absolute;top:380px;left:1140px;writing-mode:vertical-rl;white-space:nowrap;color:#fff;font-size:11px;letter-spacing:.2em;line-height:1}

.news{position:absolute;top:752px;left:128px;width:952px;height:176px;background:#fff;box-shadow:0 4px 18px rgba(0,0,0,.12);display:flex;align-items:center}
.news-head{width:230px;text-align:center}
.news-head .en{font-size:13px;letter-spacing:.2em;color:var(--muted)}
.news-head .ja{font-size:24px;font-weight:700}
.news-list{list-style:none;border-left:1px solid var(--line);padding-left:40px}
.news-list li{font-size:14px;line-height:2.4;display:flex;gap:22px;align-items:center}
.news-list .date{color:var(--muted);width:90px}
.tag{background:var(--ink);color:#fff;font-size:11px;padding:2px 8px;line-height:1.4}
.tag--blank{visibility:hidden}

.ramen{position:absolute;top:990px;left:128px;display:flex;gap:90px;align-items:center}
.ramen-photo{width:344px;height:184px;background:linear-gradient(135deg,#e9d9b8,#c98b45 55%,#8d4a24)}
.ramen-text .lead{font-size:16px}
.ramen-text h2{font-size:30px;font-weight:700;margin:6px 0 16px}
.ramen-text p{font-size:13px;line-height:1.9;color:#555;width:340px}

.menu-band{position:absolute;top:1220px;left:0;width:1200px;height:640px;background:linear-gradient(160deg,#4a2d1c,#7c5232 50%,#2d1c14);clip-path:polygon(0 14%,100% 0,100% 86%,0 100%)}
.menu-title{position:absolute;top:1390px;left:0;width:1200px;text-align:center;color:#fff}
.menu-title .en{font-size:13px;letter-spacing:.3em}
.menu-title .ja{font-size:30px;font-weight:700}
.menu-card{position:absolute;top:1488px;width:464px;height:364px;background:#fff;box-shadow:0 4px 18px rgba(0,0,0,.18);padding:34px 40px}
.menu-card ul{list-style:none}
.menu-card li{font-size:16px;line-height:50px;display:flex;align-items:center;gap:16px}
.menu-card li::before{content:"";width:12px;height:12px;background:var(--ink)}

.info{position:absolute;top:1900px;left:0;width:1200px;height:580px;background:var(--paper)}
.info-title{position:absolute;top:1940px;left:0;width:1200px;text-align:center}
.info-title .en{font-size:12px;letter-spacing:.3em;color:var(--muted)}
.info-title .ja{font-size:30px;font-weight:700}
.store{position:absolute;top:2040px;width:440px}
.store h3{text-align:center;font-size:22px;font-weight:500;margin-bottom:14px}
.store .map{height:172px;background:linear-gradient(135deg,#e6ece4,#d3ddd0)}
.store dl{margin-top:36px;display:grid;grid-template-columns:90px 1fr;row-gap:12px;font-size:13px;line-height:1.6}
.store dt{font-weight:700}

.cta{position:absolute;top:2518px;left:0;width:1200px;display:flex;justify-content:center;gap:20px}
.site-footer{position:absolute;bottom:0;left:0;width:1200px;height:48px;background:var(--dark);color:#fff;font-size:12px;display:flex;align-items:center;justify-content:center;letter-spacing:.1em}
</style>
</head>
<body>
<header class="site-header">
  <div class="logo">店名ロゴが入ります</div>
  <div class="btns"><a class="btn btn--orange">ツマミドリはこちら</a><a class="btn btn--red">味ノートはこちら</a></div>
</header>

<section class="hero" role="img" aria-label="鰹節がのったお好み焼きの写真">
  <div class="hero-line hero-line--1 serif">ふんわり</div>
  <div class="hero-line hero-line--2 serif">じゅわっと</div>
  <div class="hero-line hero-line--sub serif">とろける味わい</div>
  <div class="hero-side">OKONOMIYAKI SINCE 2000</div>
</section>

<section class="news">
  <div class="news-head"><div class="en">NEWS</div><div class="ja serif">お知らせ</div></div>
  <ul class="news-list">
    <li><span class="date">2021.01.20</span><span class="tag">NEW</span>ホームページを公開しました</li>
    <li><span class="date">2021.01.15</span><span class="tag tag--blank">NEW</span>お知らせが入ります。</li>
    <li><span class="date">2021.01.10</span><span class="tag tag--blank">NEW</span>お知らせが入ります。</li>
  </ul>
</section>

<section class="ramen">
  <div class="ramen-photo" role="img" aria-label="ラーメンの写真"></div>
  <div class="ramen-text">
    <div class="lead serif">お好み焼き屋で？</div>
    <h2 class="serif">ラーメンはじめました！</h2>
    <p>当店自慢の出汁を活かした、こだわりのラーメンを始めました。ぜひ一度ご賞味ください。</p>
  </div>
</section>

<div class="menu-band" role="img" aria-label="お好み焼きの写真"></div>
<div class="menu-title serif"><div class="en">MENU</div><div class="ja">お品メニュー</div></div>
<div class="menu-card" style="left:128px"><ul>
  <li>お好み焼きのメニュー名入ります。</li><li>お好み焼きのメニュー名入ります。</li><li>お好み焼きのメニュー名入ります。</li><li>お好み焼きのメニュー名入ります。</li><li>お好み焼きのメニュー名入ります。</li><li>お好み焼きのメニュー名入ります。</li>
</ul></div>
<div class="menu-card" style="left:608px"><ul>
  <li>お好み焼きのメニュー名入ります。</li><li>お好み焼きのメニュー名入ります。</li><li>お好み焼きのメニュー名入ります。</li><li>お好み焼きのメニュー名入ります。</li><li>お好み焼きのメニュー名入ります。</li><li>お好み焼きのメニュー名入ります。</li>
</ul></div>

<section class="info"></section>
<div class="info-title serif"><div class="en">INFORMATION</div><div class="ja">店舗情報</div></div>
<div class="store" style="left:128px">
  <h3 class="serif">支店名が入ります</h3>
  <div class="map" role="img" aria-label="店舗周辺の地図"></div>
  <dl><dt>住所</dt><dd>〒000-0000<br>ここに住所が入ります。ここに住所が入ります。</dd><dt>電話番号</dt><dd>00-0000-0000</dd><dt>営業時間</dt><dd>00:00〜00:00</dd></dl>
</div>
<div class="store" style="left:628px">
  <h3 class="serif">支店名が入ります</h3>
  <div class="map" role="img" aria-label="店舗周辺の地図"></div>
  <dl><dt>住所</dt><dd>〒000-0000<br>ここに住所が入ります。ここに住所が入ります。</dd><dt>電話番号</dt><dd>00-0000-0000</dd><dt>営業時間</dt><dd>00:00〜00:00</dd></dl>
</div>

<div class="cta"><a class="btn btn--orange">ツマミドリはこちら</a><a class="btn btn--red">味ノートはこちら</a></div>
<footer class="site-footer">© 店名が入ります</footer>
</body>
</html>
```